VerdaTurfix - 11" x 4" Door Hanger, full color both sides

We need a door hanger designed, 11" x 4", full color both sides, We are a lawn care company that provides lawn mowing, and other services to clients. This door hanger will be place on the 9 neighbors of our current clients. The ad needs to state that we provided lawn service to one of their neighbors today, and that we are in their neighborhood each week on that day. The door hanger will have 4 printings, substituting the day of Tuesday, Wednesday, Thursday, and Friday. All the art work and text will remain the same except the day of the week. For information about VerdaTurfix, please visit our website www.verdaturfix.net. The main emphasis of the message should be that we are their every week on that day, and the benefits to them of using our service (ie. quality time with their family, golf, sports, resting, etc., instead of mowing the lawn). At the bottom of the door hanger will be a coupon offering their tenth (10th) lawn service free, which is the same as a 10% discount.

I have uploaded a template files for the front and back of an 11 x 4 door hanger, The templates are pdf, jpeg, or eps files. The final product can be a pdf, jpeg, or eps file.

Target Market(s)

Neighbors of our existing clients

Industry/Entity Type

Lawn Care

Font styles to use
Serif

Requirements
Must have
• Professional design and art, Short conversational message that relays the following thoughts:
• 1. We mowed your neighbor's lawn today!
• 2. We are in your neighborhood every Tuesday!
• 3. Our lawn service is guaranteed.
• 4. Call to action - Call us today! 555-014-7382
• 5. Of course our contact info, name, phone number, website address.
• 6. Coupon at bottom for "10th lawn service Free!"
Nice to have
• Art work from our website is fine to use, That carries our theme throughout our campaign.
Should not have
• Very wordy. This is basically a billboard, Have very few seconds to grab their attention.

```html
<!DOCTYPE html>
<html lang="en">
<head>
<meta charset="utf-8">
<title>VerdaTurfix Door Hanger</title>
<link href="https://fonts.googleapis.com/css2?family=Roboto+Condensed:wght@400;700&display=swap" rel="stylesheet">
<style>
  :root {
    --grass-dark: #3f7a1f;
    --grass-mid: #6fa83a;
    --grass-light: #b9d98a;
    --veil: rgba(255, 255, 255, 0.72);
    --guide-red: #e0242c;
    --guide-blue: #2b3990;
    --guide-green: #22a84a;
    --ink: #1a1a1a;
    --accent: #2f6b14;
    --pill: #111111;
    --coupon: #fff200;
    --white: #ffffff;
  }
  * { margin: 0; padding: 0; box-sizing: border-box; }
  html, body { width: 1200px; height: 2880px; overflow: hidden; }
  body { font-family: "Roboto Condensed", "Arial Narrow", sans-serif; color: var(--ink); }
  .hanger { position: relative; width: 1200px; height: 2880px; overflow: hidden; }
  .lawn-backdrop {
    position: absolute; inset: 0;
    background: radial-gradient(ellipse at 50% 40%, var(--grass-light) 0%, var(--grass-mid) 45%, var(--grass-dark) 100%);
  }
  .guides { position: absolute; inset: 0; }
  .visit-note {
    position: absolute; left: 160px; top: 178px; width: 880px;
    text-align: center; font-size: 48px; line-height: 58px; font-weight: 700; color: var(--accent);
  }
  .family-photo {
    position: absolute; left: 157px; top: 750px; width: 476px; height: 910px;
    border-radius: 40px;
    background: linear-gradient(180deg, #9cc27a 0%, #e9e4dc 40%, #c9d8c0 65%, #5f9a35 100%);
  }
  .benefit {
    position: absolute; left: 650px; top: 815px;
    font-size: 72px; line-height: 127px; font-weight: 400;
  }
  .promise {
    position: absolute; left: 650px; top: 1380px; width: 390px;
    font-size: 56px; line-height: 66px; font-weight: 700; color: var(--accent);
  }
  .call-to-action {
    position: absolute; left: 650px; top: 1530px; width: 390px;
    font-size: 50px; line-height: 60px; font-weight: 400;
  }
  .call-to-action strong { font-weight: 700; font-size: 56px; }
  .tagline {
    position: absolute; left: 153px; top: 1707px; width: 900px; height: 86px;
    border-radius: 43px; background: var(--pill); color: var(--white);
    font-size: 52px; font-weight: 700; line-height: 86px; text-align: center;
  }
  .contact {
    position: absolute; left: 157px; top: 1862px; font-style: normal;
    font-size: 72px; line-height: 86px; font-weight: 400;
  }
  .coupon {
    position: absolute; left: 150px; top: 2227px; width: 903px; height: 513px;
    border: 10px dashed var(--ink); border-radius: 60px;
    padding: 12px;
  }
  .coupon-fill {
    width: 100%; height: 100%; border-radius: 46px; background: var(--coupon);
    text-align: center;
  }
  .coupon-headline { font-size: 196px; line-height: 200px; padding-top: 18px; font-weight: 400; }
  .coupon-offer { font-size: 104px; line-height: 112px; font-weight: 400; }
</style>
</head>
<body>
<main class="hanger">
  <div class="lawn-backdrop" role="img" aria-label="Close-up photograph of lush green grass blades"></div>

  <svg class="guides" width="1200" height="2880" viewBox="0 0 1200 2880">
    <rect class="panel-veil" x="120" y="120" width="960" height="2640" rx="73" fill="var(--veil)" stroke="var(--guide-blue)" stroke-width="6"/>
    <rect class="safe-line" x="150" y="150" width="900" height="2583" rx="52" fill="none" stroke="var(--guide-green)" stroke-width="6"/>
    <line class="trim-line" x1="90" y1="0" x2="90" y2="2880" stroke="var(--guide-red)" stroke-width="3"/>
    <line class="trim-line" x1="1110" y1="0" x2="1110" y2="2880" stroke="var(--guide-red)" stroke-width="3"/>
    <line class="trim-line" x1="0" y1="73" x2="1200" y2="73" stroke="var(--guide-red)" stroke-width="3"/>
    <line class="trim-line" x1="0" y1="2793" x2="1200" y2="2793" stroke="var(--guide-red)" stroke-width="3"/>
    <line class="slit-line" x1="150" y1="480" x2="432" y2="480" stroke="var(--guide-green)" stroke-width="6"/>
    <line class="slit-line" x1="150" y1="507" x2="432" y2="507" stroke="var(--guide-green)" stroke-width="6"/>
    <line class="slit-line" x1="150" y1="488" x2="455" y2="488" stroke="var(--guide-blue)" stroke-width="5"/>
    <line class="slit-line" x1="150" y1="499" x2="455" y2="499" stroke="var(--guide-blue)" stroke-width="5"/>
    <circle class="hole-safe" cx="617" cy="493" r="190" fill="var(--veil)" stroke="var(--guide-green)" stroke-width="6"/>
    <circle class="hole-trim" cx="617" cy="493" r="165" fill="none" stroke="var(--guide-blue)" stroke-width="6"/>
    <circle class="hole-cut" cx="617" cy="493" r="140" fill="none" stroke="var(--guide-red)" stroke-width="6"/>
  </svg>

  <p class="visit-note">We mowed your neighbor's lawn today!<br>We're in your neighborhood every Tuesday!</p>

  <div class="family-photo" role="img" aria-label="Photograph of a family playing with a ball together on a green lawn"></div>

  <p class="benefit">You spend<br>quality time<br>with<br>your family!</p>

  <p class="promise">Guaranteed<br>lawn service!</p>

  <p class="call-to-action">Call us today!<br><strong>555-014-7382</strong></p>

  <p class="tagline">We take care of your Lawn service.</p>

  <address class="contact">VerdaTurfix<br>P. O. Box 4821<br>Millbrook, TX 75099<br>www.verdaturfix.net</address>

  <section class="coupon">
    <div class="coupon-fill">
      <h2 class="coupon-headline">FREE!</h2>
      <p class="coupon-offer">Your 1/10th Lawn<br>service Free!</p>
    </div>
  </section>
</main>
</body>
</html>
```